Dewleaf Botanica. Home based organic skin care manufacturer

We need top notch user friendly and interactive web6/mobile site that will cater to online e commerce, retail of our varieties of products and real time communication with online buyers.

```html
<!DOCTYPE html>
<html lang="en">
<head>
<meta charset="utf-8">
<title>Dewleaf Botanica — Skin Made Perfect</title>
<link rel="stylesheet" href="https://fonts.googleapis.com/css2?family=Poppins:wght@400;500;600;700;800&family=Open+Sans:wght@400;600&family=Roboto:wght@400;500&display=swap">
<style>
:root{
  --hero:#c99484;
  --hero-dark:#a96f61;
  --brand:#b06f60;
  --band:#a1675c;
  --blush:#efcabd;
  --ink:#2b2b2b;
  --muted:#555;
  --card:#f5f4f4;
  --star:#f5a623;
  --green:#5e9a58;
  --footer:#1f1f1f;
  --white:#fff;
}
*{box-sizing:border-box;margin:0;padding:0}
html,body{width:1200px;height:3655px;overflow:hidden;background:var(--white)}
body{font-family:"Open Sans",sans-serif;color:var(--ink)}
.page{position:relative;width:1200px;height:3655px;overflow:hidden}
.abs{position:absolute}
.logo{position:absolute;display:flex;align-items:center;gap:10px;font-family:"Poppins",sans-serif;font-weight:500;letter-spacing:1px;text-transform:uppercase}
.logo .mark{width:14px;height:14px;border-radius:50%;border:2px solid currentColor}

/* hero */
.hero{position:absolute;left:0;top:0;width:1200px;height:540px;background:linear-gradient(90deg,#c48c7b 0%,#cfa091 55%,#c08879 100%)}
.hero .logo{left:113px;top:40px;font-size:15px;color:#2a2a2a}
.nav{position:absolute;top:40px;left:0;font-size:15px;color:#3a2d2a}
.nav span{position:absolute;white-space:nowrap}
.cart{position:absolute;left:1062px;top:38px}
.hero h1{position:absolute;left:112px;top:188px;font-family:"Poppins",sans-serif;font-weight:800;font-size:52px;color:var(--white);letter-spacing:-.5px}
.hero p{position:absolute;left:112px;top:268px;width:420px;font-size:22px;line-height:34px;color:#fbefe9}
.btn-outline{position:absolute;border:2px solid var(--white);border-radius:30px;color:var(--white);font-family:"Poppins",sans-serif;font-weight:700;font-size:15px;display:flex;align-items:center;justify-content:center}
.hero .btn-outline{left:113px;top:360px;width:122px;height:45px}
.hero-product{position:absolute;left:735px;top:166px;width:227px;height:416px;border-radius:40px 40px 30px 30px;background:linear-gradient(180deg,#eeeeee 0 22%,#e9c94c 22% 100%);box-shadow:0 10px 25px rgba(0,0,0,.18)}
.dots{position:absolute;left:578px;top:482px;display:flex;gap:8px}
.dots i{width:10px;height:10px;border-radius:50%;background:#fff}
.dots i.on{background:#e7b94a}
.torn{position:absolute;left:0;width:1200px}

/* headings */
.section-title{position:absolute;left:0;width:1200px;text-align:center;font-family:"Poppins",sans-serif;font-weight:600;font-size:28px;color:var(--ink)}

/* single picks */
.pick{position:absolute;top:755px;width:231px;height:353px;background:var(--card);border-radius:4px;text-align:center}
.pick .img{position:absolute;left:2px;top:2px;width:227px;height:166px;background:var(--white)}
.pick .img i{position:absolute;left:50%;top:18px;transform:translateX(-50%);border-radius:8px}
.pick .name{position:absolute;top:195px;width:100%;font-size:17px}
.stars{color:var(--star);font-size:13px;letter-spacing:1px}
.pick .stars{position:absolute;top:222px;width:100%}
.pick .price{position:absolute;top:251px;width:100%;font-size:18px}
.btn-fill{position:absolute;left:49px;top:295px;width:133px;height:39px;border-radius:22px;background:var(--brand);color:#fff;font-family:"Poppins",sans-serif;font-weight:600;font-size:13px;display:flex;align-items:center;justify-content:center;box-shadow:0 3px 6px rgba(0,0,0,.15)}
.arrow-btn{position:absolute;width:52px;height:52px;border-radius:50%;display:flex;align-items:center;justify-content:center}

/* welcome */
.welcome{position:absolute;left:0;top:1214px;width:1200px;height:500px;background:radial-gradient(circle at 25% 45%,#b87a7a 0,#a1675c 55%)}
.welcome h2{position:absolute;left:112px;top:112px;font-family:"Poppins",sans-serif;font-weight:600;font-size:29px;color:#fff}
.welcome p{position:absolute;left:112px;top:176px;width:474px;font-size:15.5px;line-height:25.7px;color:#fbeee9;text-align:justify}
.welcome .btn-outline{left:112px;top:386px;width:148px;height:46px}
.photo-frame{position:absolute;left:628px;top:94px;width:461px;height:325px;background:#fff;padding:8px}
.photo-frame div{width:100%;height:100%;background:linear-gradient(160deg,#f1efec,#d9d6d2 60%,#8a7f78)}

/* kits */
.kit{position:absolute;top:1932px;width:298px;height:386px;background:var(--card)}
.kit .img{position:absolute;left:0;top:0;width:298px;height:299px;background:#fafafa}
.kit .img i{position:absolute;left:88px;top:38px;width:122px;height:222px;border-radius:22px}
.kit .name{position:absolute;top:322px;width:100%;text-align:center;font-family:"Poppins",sans-serif;font-weight:500;font-size:17px}
.kit .price{position:absolute;top:350px;width:100%;text-align:center;font-family:"Poppins",sans-serif;font-size:14px;color:var(--brand)}

/* testimonial */
.testimonial{position:absolute;left:0;top:2407px;width:1200px;height:440px;background:var(--blush)}
.testimonial h2{position:absolute;top:68px;width:100%;text-align:center;font-family:"Poppins",sans-serif;font-weight:600;font-size:29px;color:#2e2e2e}
.avatar{position:absolute;left:169px;top:194px;width:156px;height:156px;border-radius:50%;border:3px solid #fff;background:linear-gradient(180deg,#e9e3dd,#cbb8a4)}
.quote-mark{position:absolute;left:372px;top:178px;font-family:Georgia,serif;font-size:80px;color:#cdb2a8;line-height:1}
.testimonial .stars{position:absolute;left:433px;top:166px;font-size:16px}
.testimonial blockquote{position:absolute;left:433px;top:206px;width:552px;font-family:"Roboto",sans-serif;font-size:15.5px;line-height:25.5px;color:#4a4a4a}
.testimonial .who{position:absolute;left:432px;top:331px;font-family:"Roboto",sans-serif;font-weight:500;font-size:18px;color:#333}
.testimonial .role{position:absolute;left:432px;top:361px;font-family:"Roboto",sans-serif;font-size:13px;color:#555}

/* features */
.feature{position:absolute;top:2979px;width:222px;height:192px;background:#fff;box-shadow:0 3px 14px rgba(0,0,0,.09);text-align:center}
.feature .icon{position:absolute;left:78px;top:26px;width:66px;height:66px;border-radius:50%;background:var(--brand);display:flex;align-items:center;justify-content:center}
.feature .label{position:absolute;top:118px;width:100%;font-family:"Poppins",sans-serif;font-weight:500;font-size:16px;line-height:27px;color:#222;text-transform:uppercase}

/* footer */
.footer{position:absolute;left:0;top:3271px;width:1200px;height:384px;background:var(--footer);color:#fff}
.footer .logo{left:113px;top:178px;font-size:19px;color:#fff;letter-spacing:2px}
.footer h4{position:absolute;font-family:"Poppins",sans-serif;font-weight:600;font-size:17px}
.footer ul{position:absolute;list-style:none;font-size:15px;line-height:25.5px}
.social{position:absolute;left:116px;top:296px;display:flex;gap:12px}
.social i{width:24px;height:24px;border-radius:50%;background:#fff;opacity:.9}
.contact-row{position:absolute;left:589px;display:flex;gap:14px;font-size:15px;line-height:25px}
.contact-row svg{flex:none;margin-top:4px}
.newsletter{position:absolute;left:864px;top:139px;width:224px;height:40px;border-radius:4px;background:#fff;overflow:hidden}
.newsletter span{position:absolute;left:14px;top:10px;font-size:14px;color:#888}
.newsletter b{position:absolute;right:0;top:0;width:54px;height:40px;background:#e8bfb0;display:flex;align-items:center;justify-content:center}
.pay{position:absolute;left:864px;top:263px;display:flex;gap:4px}
.pay i{width:33px;height:21px;border-radius:2px;background:#d9d9d9}
.copyright{position:absolute;top:332px;width:1200px;text-align:center;font-size:15px;color:#e8e8e8}
</style>
</head>
<body>
<div class="page">

  <!-- hero -->
  <section class="hero">
    <div class="logo"><span class="mark"></span>Dewleaf Botanica</div>
    <nav class="nav">
      <span style="left:498px">Home</span>
      <span style="left:577px">About Us</span>
      <span style="left:679px">Shop</span>
      <span style="left:752px">Blog</span>
      <span style="left:820px">Distributors</span>
      <span style="left:940px">Contacts</span>
    </nav>
    <svg class="cart" width="24" height="22" viewBox="0 0 24 22"><path d="M0 1h4l3 12h13l3-9H6" fill="none" stroke="#2a2a2a" stroke-width="2.4"/><path d="M6 4h17l-3 9H8z" fill="#2a2a2a"/><circle cx="9" cy="18" r="2.2" fill="#2a2a2a"/><circle cx="19" cy="18" r="2.2" fill="#2a2a2a"/></svg>
    <h1>SKIN MADE PERFECT</h1>
    <p>Give your skin the new look and feel it deserves</p>
    <div class="btn-outline">SHOP</div>
    <div class="dots"><i></i><i class="on"></i><i></i></div>
  </section>
  <svg class="torn" style="top:500px" height="60" viewBox="0 0 1200 60" preserveAspectRatio="none"><path d="M0 30 L40 22 70 34 110 26 150 38 200 28 240 36 290 24 330 34 380 30 420 40 470 28 520 36 560 26 610 38 660 30 700 22 760 36 800 28 850 38 900 26 950 34 1000 24 1040 36 1090 28 1140 20 1170 30 1200 12 L1200 60 0 60Z" fill="#fff"/></svg>
  <div class="hero-product" role="img" aria-label="Face glow elixir bottle with white cap and yellow botanical label"></div>

  <!-- single picks -->
  <h2 class="section-title" style="top:658px">SINGLE PICKS</h2>
  <div class="arrow-btn" style="left:41px;top:879px;background:#fff;box-shadow:0 2px 8px rgba(0,0,0,.15)"><svg width="12" height="18" viewBox="0 0 12 18"><path d="M10 2 3 9l7 7" fill="none" stroke="#5e9a58" stroke-width="2.4"/></svg></div>
  <div class="arrow-btn" style="left:1107px;top:879px;background:var(--green)"><svg width="12" height="18" viewBox="0 0 12 18"><path d="M2 2l7 7-7 7" fill="none" stroke="#fff" stroke-width="2.4"/></svg></div>

  <article class="pick" style="left:112px">
    <div class="img"><i role="img" aria-label="Age reverse serum jar" style="width:72px;height:130px;background:linear-gradient(180deg,#ddd 0 18%,#efe6cf 18%)"></i></div>
    <div class="name">Skin Fix Milk</div><div class="stars">★★★★★</div><div class="price">$16.00</div>
    <div class="btn-fill">ADD TO CART</div>
  </article>
  <article class="pick" style="left:360px">
    <div class="img"><i role="img" aria-label="Clear liquid soap bottle" style="width:44px;height:130px;background:linear-gradient(180deg,#e4e4e4,#f7f7f7)"></i></div>
    <div class="name">Kiddies Soap</div><div class="stars">★★★★★</div><div class="price">$16.00</div>
    <div class="btn-fill">ADD TO CART</div>
  </article>
  <article class="pick" style="left:608px">
    <div class="img"><i role="img" aria-label="Amber pump bottle" style="width:40px;height:130px;background:linear-gradient(180deg,#222 0 18%,#8a3f22 18%,#b4633a)"></i></div>
    <div class="name">Fruity whitening</div><div class="stars">★★★★★</div><div class="price">$16.00</div>
    <div class="btn-fill">ADD TO CART</div>
  </article>
  <article class="pick" style="left:856px">
    <div class="img"><i role="img" aria-label="Lavender cream jar with olive lid" style="top:34px;width:108px;height:100px;background:linear-gradient(180deg,#a3a13c 0 30%,#c7b1d6 30%)"></i></div>
    <div class="name">Anti Dandruff Shampoo</div><div class="stars">★★★★★</div><div class="price">$16.00</div>
    <div class="btn-fill">ADD TO CART</div>
  </article>

  <!-- welcome -->
  <section class="welcome">
    <h2>WELCOME TO DEWLEAF BOTANICA</h2>
    <p>My early intense love for everything natural skin care inspired the birth of Dewleaf Botanica. I'm a strong believer of nature and that's why, in addition to my expertise as a certified organic skin care products formulator, I daily explore more natural ingredients to care for your skin and hair. The future is green. The future is now and so is DB. Welcome to my habitat....<br>Marisol, Founder, Dewleaf Botanica</p>
    <div class="btn-outline">LEARN MORE</div>
    <div class="photo-frame"><div role="img" aria-label="Makeup brushes standing in a glass cup"></div></div>
  </section>
  <svg class="torn" style="top:1660px" height="70" viewBox="0 0 1200 70" preserveAspectRatio="none"><path d="M0 38 L50 30 90 44 140 32 190 46 240 34 290 42 340 30 390 44 440 36 490 46 540 32 590 42 640 34 690 46 740 36 790 44 840 30 890 42 940 34 990 44 1040 32 1090 40 1130 20 1160 12 1200 4 L1200 70 0 70Z" fill="#fff"/></svg>

  <!-- kits -->
  <h2 class="section-title" style="top:1837px">KITS</h2>
  <article class="kit" style="left:112px">
    <div class="img"><i role="img" aria-label="Yellow face glow elixir bottle" style="background:linear-gradient(180deg,#e6e6e6 0 20%,#e8c84c 20%)"></i></div>
    <div class="name">Rejuvenating Hair Kit</div><div class="price">$34.95</div>
  </article>
  <article class="kit" style="left:450px">
    <div class="img"><i role="img" aria-label="Cream brightening face and body bottle" style="background:linear-gradient(180deg,#e6e6e6 0 20%,#f1e8d3 20%)"></i></div>
    <div class="name">Kiddies Glow Kit</div><div class="price">$34.95</div>
  </article>
  <article class="kit" style="left:788px">
    <div class="img"><i role="img" aria-label="White brightening body milk bottle" style="background:linear-gradient(180deg,#e6e6e6 0 20%,#f6f5f8 20%)"></i></div>
    <div class="name">Pop 'n' Glow Kit</div><div class="price">$34.95</div>
  </article>

  <!-- testimonial -->
  <section class="testimonial">
    <h2>WHAT PEOPLE SAY</h2>
    <svg class="abs" style="left:74px;top:255px" width="20" height="34" viewBox="0 0 20 34"><path d="M17 2 3 17l14 15" fill="none" stroke="#222" stroke-width="3"/></svg>
    <svg class="abs" style="left:1110px;top:255px" width="20" height="34" viewBox="0 0 20 34"><path d="M3 2l14 15L3 32" fill="none" stroke="#222" stroke-width="3"/></svg>
    <div class="avatar" role="img" aria-label="Portrait of the reviewer"></div>
    <div class="quote-mark">“</div>
    <div class="stars">★★★★★</div>
    <blockquote>A lot of people have been asking what i use on mu skin.I use to have serious dark spots and acne after i gave birth and i gave up untill i came in contact with dewleaf botanica. Their products dont' bleach the skin. I.m even more beautiful in real life.</blockquote>
    <div class="who">Adaeze Nwosu</div>
    <div class="role">Ceo, Blush &amp; Bloom</div>
  </section>
  <svg class="torn" style="top:2800px" height="60" viewBox="0 0 1200 60" preserveAspectRatio="none"><path d="M0 20 L40 30 90 22 140 34 190 24 240 36 290 26 340 34 390 22 440 32 490 26 540 36 590 24 640 34 690 26 740 36 790 22 840 32 890 24 940 34 990 26 1040 32 1090 22 1140 30 1200 20 L1200 60 0 60Z" fill="#fff"/></svg>

  <!-- features -->
  <div class="feature" style="left:108px">
    <div class="icon"><svg width="34" height="24" viewBox="0 0 34 24" fill="none" stroke="#fff" stroke-width="1.8"><path d="M2 3h18v14H2zM20 8h7l5 6v3h-12"/><circle cx="8" cy="19" r="3" fill="#b06f60"/><circle cx="26" cy="19" r="3" fill="#b06f60"/></svg></div>
    <div class="label">Fast &amp; Prompt<br>Delivery</div>
  </div>
  <div class="feature" style="left:360px">
    <div class="icon"><svg width="32" height="26" viewBox="0 0 32 26" fill="none" stroke="#fff" stroke-width="1.8"><rect x="2" y="6" width="22" height="16" rx="2"/><path d="M2 11h22"/><path d="M24 2l6 3v6c0 4-3 6-6 7"/><path d="M22 8l2 2 3-4"/></svg></div>
    <div class="label">Secure Payment</div>
  </div>
  <div class="feature" style="left:611px">
    <div class="icon"><svg width="30" height="30" viewBox="0 0 30 30" fill="none" stroke="#fff" stroke-width="1.8"><circle cx="15" cy="15" r="12"/><circle cx="15" cy="15" r="8"/><path d="M11 15l3 3 5-6"/></svg></div>
    <div class="label">100% Guaranteed</div>
  </div>
  <div class="feature" style="left:864px">
    <div class="icon"><svg width="30" height="30" viewBox="0 0 30 30" fill="none" stroke="#fff" stroke-width="1.8"><circle cx="17" cy="10" r="7"/><path d="M17 6v8M15 8h4M2 22h6l5 3h8l7-5-2-2-6 3h-5"/></svg></div>
    <div class="label">Money Back<br>Guaranteed</div>
  </div>

  <!-- footer -->
  <footer class="footer">
    <div class="logo"><span class="mark"></span>Dewleaf Botanica</div>
    <div class="social"><i></i><i></i><i></i></div>

    <h4 style="left:406px;top:88px">QUICK LINKS</h4>
    <ul style="left:406px;top:133px"><li>Home</li><li>About Us</li><li>Shop</li><li>Blog</li><li>Distributors</li><li>Contacts</li></ul>

    <h4 style="left:589px;top:88px">CONTACT US</h4>
    <div class="contact-row" style="top:142px"><svg width="14" height="20" viewBox="0 0 14 20"><path d="M7 0a7 7 0 0 0-7 7c0 5 7 13 7 13s7-8 7-13a7 7 0 0 0-7-7z" fill="#fff"/><circle cx="7" cy="7" r="2.5" fill="#1f1f1f"/></svg><span>Lorem ipsum dolor<br>sit amet, consectetur</span></div>
    <div class="contact-row" style="top:205px"><svg width="16" height="16" viewBox="0 0 16 16"><path d="M3 0l3 4-2 2c1 2 3 4 6 6l2-2 4 3-2 3C7 16 0 9 0 2z" fill="#fff"/></svg><span>+(234) 800 555 0142</span></div>
    <div class="contact-row" style="top:239px"><svg width="18" height="13" viewBox="0 0 18 13"><rect width="18" height="13" rx="1" fill="#fff"/><path d="M1 1l8 6 8-6" fill="none" stroke="#1f1f1f" stroke-width="1.5"/></svg><span>hello@dewleafbotanica.com</span></div>

    <h4 style="left:864px;top:88px">NEWSLETTER</h4>
    <div class="newsletter"><span>Enter email</span><b><svg width="16" height="12" viewBox="0 0 16 12"><rect width="16" height="12" rx="1" fill="#1f1f1f"/><path d="M1 1l7 5 7-5" fill="none" stroke="#e8bfb0" stroke-width="1.4"/></svg></b></div>
    <h4 style="left:864px;top:220px">PAYMENT OPTION</h4>
    <div class="pay"><i></i><i></i><i></i><i></i><i></i><i></i></div>

    <div class="copyright">©Copyrights 2023 Dewleaf Botanica &nbsp;&nbsp;| &nbsp;&nbsp;All Rights Reserved</div>
  </footer>
</div>
</body>
</html>
```